Professional individual needs business card design

I need a business card designed for my friend to show their skills and contact details

I would like to see pattern designs with a black foreground and strong look - will submit content specifics but basics are:

NAME SURNAME (large and bold)
Event Manager & MC

Tressel Magazine
The other event I run

phone number - email

```html
<!DOCTYPE html>
<html lang="en">
<head>
<meta charset="UTF-8">
<title>Business Card – Event Manager &amp; MC</title>
<link rel="stylesheet" href="https://fonts.googleapis.com/css2?family=Source+Sans+3:wght@400;600;700&display=swap">
<style>
  :root {
    --bg-top: #2e2d2d;
    --bg-bottom: #1f1e1e;
    --accent: #8cc63f;
    --text: #ffffff;
    --icon-cut: #262525;
  }
  html, body {
    margin: 0;
    padding: 0;
    width: 1200px;
    height: 720px;
    overflow: hidden;
    background: var(--bg-bottom);
  }
  .card {
    position: relative;
    width: 1200px;
    height: 720px;
    overflow: hidden;
    background: linear-gradient(180deg, var(--bg-top) 0%, var(--bg-bottom) 100%);
    font-family: "Source Sans 3", "Myriad Pro", sans-serif;
    color: var(--text);
  }
  .identity {
    position: absolute;
    left: 619px;
    top: 94px;
  }
  .identity__name {
    margin: 0;
    font-size: 53px;
    font-weight: 700;
    letter-spacing: 0.6px;
    color: var(--accent);
    line-height: 1;
  }
  .identity__role {
    margin: 10px 0 0 3px;
    font-size: 32px;
    font-weight: 400;
    line-height: 1;
  }
  .rule {
    position: absolute;
    top: 357px;
    height: 4px;
    background: var(--accent);
  }
  .rule--left { left: 0; width: 101px; }
  .rule--right { left: 618px; width: 582px; }
  .brand {
    position: absolute;
    left: 124px;
    top: 321px;
    margin: 0;
    font-size: 74px;
    font-weight: 600;
    line-height: 1;
    color: var(--accent);
  }
  .address {
    position: absolute;
    left: 618px;
    top: 417px;
    margin: 0;
    font-style: normal;
    font-size: 33px;
    line-height: 40.5px;
    letter-spacing: 0.2px;
  }
  .contacts {
    position: absolute;
    left: 618px;
    top: 530px;
    margin: 0;
    padding: 0;
    list-style: none;
    font-size: 33px;
    letter-spacing: 0.2px;
  }
  .contacts__item {
    display: flex;
    align-items: center;
    height: 40.5px;
  }
  .contacts__icon {
    width: 28px;
    height: 28px;
    margin-right: 24px;
    flex: none;
  }
</style>
</head>
<body>
  <main class="card">
    <header class="identity">
      <h1 class="identity__name">NAME SURNAME</h1>
      <p class="identity__role">Event Manager &amp; MC</p>
    </header>

    <div class="rule rule--left"></div>
    <p class="brand">Brightfold</p>
    <div class="rule rule--right"></div>

    <address class="address">
      P.O. Box: 1234, Marlow Street,<br>
      London, United Kingdom
    </address>

    <ul class="contacts">
      <li class="contacts__item">
        <svg class="contacts__icon" viewBox="0 0 28 28" aria-hidden="true">
          <path d="M3 10c0-4 5-6 11-6s11 2 11 6v2h-6v-3H9v3H3z" fill="#8cc63f"/>
          <path d="M8 13h12l4 10H4z" fill="#8cc63f"/>
          <circle cx="14" cy="18" r="3" fill="#262525"/>
        </svg>
        <span>Tel: 0099 5550184723</span>
      </li>
      <li class="contacts__item">
        <svg class="contacts__icon" viewBox="0 0 28 28" aria-hidden="true">
          <rect x="8" y="3" width="12" height="7" fill="#8cc63f"/>
          <rect x="3" y="11" width="22" height="10" rx="2" fill="#8cc63f"/>
          <rect x="8" y="17" width="12" height="8" fill="#8cc63f" stroke="#262525" stroke-width="1.5"/>
        </svg>
        <span>Fax: 0099 5550184723</span>
      </li>
      <li class="contacts__item">
        <svg class="contacts__icon" viewBox="0 0 28 28" aria-hidden="true">
          <rect x="2" y="6" width="24" height="17" fill="#8cc63f"/>
          <path d="M2 6l12 10L26 6" fill="none" stroke="#262525" stroke-width="1.8"/>
        </svg>
        <span>Email: info@brightfold.com</span>
      </li>
      <li class="contacts__item">
        <svg class="contacts__icon" viewBox="0 0 28 28" aria-hidden="true" fill="none" stroke="#8cc63f" stroke-width="2">
          <circle cx="14" cy="14" r="11"/>
          <ellipse cx="14" cy="14" rx="5" ry="11"/>
          <path d="M3 14h22M5 8h18M5 20h18M14 3v22"/>
        </svg>
        <span>Web: www.brightfold.com</span>
      </li>
    </ul>
  </main>
</body>
</html>
```